Fiscal Sponsorship Program Flyer

We are seeking a designer to create a 1-2 flyer that explains our fiscal sponsorship program. This flyer will be used to recruit new projects that might be interested in utilizing our fiscal sponsorship services. The pertinent information about our program can be found in the attached PDF. For users who cannot access the PDF, please try this link: https://files.brivanto.net/slides/d/7QtR2wXkLmZp9HvCs4YdNe8JfGaUoBi3Tx5Wl0KyRc2s/view?mode=shared

Target Market(s)

New charitable projects that do not yet have their own 501(c)(3) status, and are seeking a fiscal sponsor.

Industry/Entity Type

Nonprofit/Charity

Requirements
Must have
• The flyer must include the language and detail included on the attached PDF. The desire is to reformat this to be more appealing and easy to read.

```html
<!DOCTYPE html>
<html lang="en">
<head>
<meta charset="utf-8">
<title>Catalyst Foundation – Fiscal Sponsorship Program</title>
<link rel="stylesheet" href="https://fonts.googleapis.com/css2?family=Montserrat:wght@300;400;500;600;700;800&family=Lato:wght@400&display=swap">
<style>
  :root {
    --navy: #2b3283;
    --navy-deep: #232a72;
    --sky: #3fa9e2;
    --ocean: #2f6bbf;
    --frame: #1f4e6e;
    --ink: #1f2a80;
    --grey: #7a7a7a;
    --grey-soft: #8a8a8a;
    --page: #ffffff;
    --backdrop: #efefef;
  }
  * { box-sizing: border-box; margin: 0; padding: 0; }
  html, body { width: 1200px; height: 1200px; overflow: hidden; background: var(--backdrop); }
  body { font-family: "Montserrat", sans-serif; }

  .flyer {
    position: absolute; left: 140px; top: 0;
    width: 920px; height: 1200px;
    background: var(--page); overflow: hidden;
  }
  .flyer__wave { position: absolute; left: 0; top: 0; width: 920px; height: 250px; }

  .brand { position: absolute; left: 75px; top: 30px; color: #fff; }
  .brand__name { font-weight: 800; font-size: 58px; line-height: 58px; letter-spacing: 0.5px; }
  .brand__tag { margin: 12px 0 0 63px; font-size: 11.5px; font-weight: 500; letter-spacing: 1.6px; }

  .section-title { position: absolute; color: var(--ink); font-weight: 700; }

  .mission__title { left: 88px; top: 276px; font-size: 25px; }
  .mission__text {
    position: absolute; left: 87px; top: 309px; width: 770px;
    font-size: 13.4px; line-height: 18px; color: var(--grey); font-weight: 400;
  }

  .pillars {
    position: absolute; left: 81px; top: 376px; width: 745px; height: 298px;
    border: 2px solid var(--frame); display: flex;
  }
  .pillar { padding: 12px 18px 0 20px; }
  .pillar + .pillar { border-left: 2px solid var(--frame); }
  .pillar--what { width: 247px; }
  .pillar--philosophy { width: 237px; padding-left: 10px; padding-right: 10px; }
  .pillar--values { flex: 1; padding-left: 14px; padding-right: 14px; }
  .pillar__title {
    color: var(--ink); font-weight: 700; font-size: 19px; line-height: 22px;
    text-align: center; margin-bottom: 17px; white-space: nowrap; letter-spacing: -0.2px;
  }
  .pillar__text {
    font-size: 12.2px; line-height: 14.2px; color: var(--grey-soft);
    text-align: justify; font-weight: 400;
  }
  .pillar--philosophy .pillar__text { padding: 0 6px; }
  .pillar__text--values { font-family: "Lato", sans-serif; font-size: 11px; color: #6f6f6f; }

  .commit__title { left: 93px; top: 698px; font-size: 20px; }
  .commit__list {
    position: absolute; left: 84px; top: 731px; width: 720px;
    list-style: none; font-size: 11.8px; line-height: 14.2px; color: var(--grey);
  }
  .commit__list li { padding-left: 10px; text-indent: -10px; }
  .commit__list li::before { content: "- "; }

  .fees__title { left: 84px; top: 856px; font-size: 25px; }
  .tier {
    position: absolute; top: 900px; width: 236px; height: 234px;
    border: 2px solid var(--navy); overflow: hidden;
  }
  .tier--basic { left: 86px; }
  .tier--standard { left: 351px; }
  .tier--premium { left: 619px; }
  .tier__head {
    height: 41px; background: var(--navy); color: #fff;
    font-weight: 600; font-size: 20px; line-height: 41px; text-align: center; white-space: nowrap;
  }
  .tier--premium .tier__head { font-size: 18.5px; }
  .tier__kind { color: var(--ink); font-weight: 700; font-size: 16px; margin: 6px 0 0 8px; }
  .tier--premium .tier__kind { margin-left: 17px; }
  .tier__list { list-style: none; font-size: 12.6px; line-height: 15.6px; color: var(--grey); font-weight: 300; margin-top: 2px; }
  .tier__list li { padding-left: 10px; text-indent: -8px; }
  .tier__list li::before { content: "- "; }
  .tier__list li.plain { padding-left: 10px; text-indent: 0; }
  .tier__list li.plain::before { content: ""; }

  .flyer__footer { position: absolute; left: 0; bottom: 0; width: 920px; height: 37px; background: var(--navy); }
</style>
</head>
<body>
<main class="flyer">
  <svg class="flyer__wave" viewBox="0 0 920 250" aria-hidden="true">
    <defs>
      <linearGradient id="band" x1="0" y1="0" x2="1" y2="0">
        <stop offset="0" stop-color="var(--sky)"/>
        <stop offset="0.7" stop-color="var(--ocean)"/>
        <stop offset="1" stop-color="var(--navy)"/>
      </linearGradient>
    </defs>
    <path fill="url(#band)" d="M0 0H920V222C870 140 810 78 745 78C600 88 455 236 300 237C180 238 70 205 0 175Z"/>
    <path fill="var(--navy-deep)" d="M0 0H920V222C880 150 830 95 770 70C640 60 500 185 330 200C200 210 80 165 0 115Z"/>
    <path fill="var(--navy)" d="M0 0H920V150C860 80 790 50 720 58C560 80 430 190 290 193C170 195 70 155 0 112Z"/>
  </svg>

  <header class="brand">
    <h1 class="brand__name">CATALYST<br>FOUNDATION</h1>
    <p class="brand__tag">FISCAL SPONSORSHIP PROGRAM</p>
  </header>

  <h2 class="section-title mission__title">MISSION &amp; VISION:</h2>
  <p class="mission__text">The Catalyst Foundation, Founded In 2010, Exists To Support Social Impact Campaigns And Organizations Through Educational, Public Engagement, And Awareness Efforts. Its Vision Is To Strengthen The Capacity Of The Social Impact Sector And Its Leaders By Providing Top-tier Fiscal Sponsorship Services.</p>

  <section class="pillars">
    <article class="pillar pillar--what">
      <h3 class="pillar__title">What is<br>Fiscal Sponsorship?</h3>
      <p class="pillar__text">Fiscal sponsorship refers to the practice of non-profit organizations offering their legal and tax-exempt status to charitable projects or groups engaged in activities related to the sponsoring organization's mission. Fiscal sponsors provide oversight, financial management, and other administrative services to build the capacity of charitable projects</p>
    </article>
    <article class="pillar pillar--philosophy">
      <h3 class="pillar__title">Fiscal Sponsorship<br>Program Philosophy</h3>
      <p class="pillar__text">We believe we can accelerate the pace and scale of social change by providing strategic back office support to emerging projects, leaders and ideas. By providing light touch administrative and capacity building services, our fiscal sponsorship program takes the administrative burden off the shoulders of leaders and their projects to allow them to focus on what they do best achieving impact and changing the world.</p>
    </article>
    <article class="pillar pillar--values">
      <h3 class="pillar__title">Organizational<br>Values</h3>
      <p class="pillar__text pillar__text--values">Trust: We believe that all successful partnerships begin with a foundation of trust.<br>Relationships:<br>Our partners are central to our work. We honor our relationships through respect, communication and transparency.<br>Embrace Complexity and Risk: We understand that bold solutions to intractable social issues often require both complexity and risk.<br>Innovation: We embrace continuous improvement, bold creativity and change.<br>Diversity: We believe that all voices matter and that effective solutions are created when decision-making is inclusive across social, cultural and economic backgrounds</p>
    </article>
  </section>

  <h2 class="section-title commit__title">CATALYST FOUNDATION - PROGRAM COMMITMENTS</h2>
  <ul class="commit__list">
    <li>Fast, simple and efficient fiscal sponsorship program</li>
    <li>Free and fast approval process - our application can be completed in 30 minutes or less. There is no fee to apply, and most projects can expect to receive a response on their application within 2 weeks</li>
    <li>No fees and no minimums; projects of any size are welcome to apply</li>
    <li>Easy onboarding process</li>
    <li>Dedicated customer service and customization of services, tailored to the individual sponsored project's needs</li>
    <li>Complex, hybrid structures, partnerships and coalitions are strongly encouraged to apply</li>
  </ul>

  <h2 class="section-title fees__title">FEE STRUCTURE:</h2>

  <section class="tier tier--basic">
    <h3 class="tier__head">Basic | Fee - 4%</h3>
    <p class="tier__kind">LIMITED</p>
    <ul class="tier__list">
      <li>Project Fund Set-Up</li>
      <li>Administration and Management</li>
      <li>Financial Management</li>
      <li>Grant Proposal Review</li>
      <li>Grant Contract Review</li>
      <li>Project Reporting</li>
      <li>Insurance</li>
      <li>Annual Audit and Form 990</li>
    </ul>
  </section>

  <section class="tier tier--standard">
    <h3 class="tier__head">Standard | Fee - 6%</h3>
    <p class="tier__kind">COMPREHENSIVE</p>
    <ul class="tier__list">
      <li>Basic Services +</li>
      <li>Customized Financial Reporting</li>
      <li>Monthly Financial Statements</li>
      <li>Subgranting/regranting to U.S. based organizations</li>
      <li>Management of Vendor and Independent Contractors (1099s)</li>
    </ul>
  </section>

  <section class="tier tier--premium">
    <h3 class="tier__head">Premium | Fee - 10% +</h3>
    <p class="tier__kind">CUSTOM</p>
    <ul class="tier__list">
      <li>Standard Services + custom services tailored to individual project needs.</li>
      <li class="plain">Customization Options:</li>
      <li>Subgranting/regranting to international organizations</li>
      <li>Lobbying Filings</li>
      <li>Project Audit</li>
      <li>Grant Writing Assistance</li>
      <li>One-on-One Coaching</li>
    </ul>
  </section>

  <footer class="flyer__footer"></footer>
</main>
</body>
</html>
```